Business Cards Needed For Veterinary Business

Looking for a business card design for a veterinary blood bank. We would like it to be clean and professional on appearance but still warm and inviting. We would like to utilize our logo and similar coloring. We will use our phone number, email, website, employee name, employee title.

We do not want a bunch of animated animal photos but do not need the style to be as clinical as a laboratory or human medical procedure office.

We are looking for some creative ideas to choose from so that we can generate a standout professional business card for our management team to utilize.

Target Market(s)

professionals

Industry/Entity Type

veterinary

Contact Information for Business Card

employee name, employee title, phone number, website URL, email

Font styles to use
Sans Serif

Colors
0054AA
0677BA
7BADD7
CADEEF
E8F1F8
EB3D1F
EC4F4E
F09395
F8D3D4
FCEDEE

Requirements
Nice to have
• creative design
Should not have
• animated photos

```html
<!DOCTYPE html>
<html lang="en">
<head>
<meta charset="utf-8">
<title>Crestline Veterinary Blood Bank – Business Card</title>
<link href="https://fonts.googleapis.com/css2?family=Montserrat:wght@400;500;700;800&display=swap" rel="stylesheet">
<style>
  :root {
    --red: #e31e2a;
    --red-soft: #ec4f4e;
    --blue: #0054aa;
    --blue-mid: #0677ba;
    --grey-text: #5a5a5a;
    --stage: #d4d4d4;
    --card-front: #fdfdfd;
    --card-back-a: #f3f3f3;
    --card-back-b: #e6e6e6;
  }
  * { margin: 0; padding: 0; box-sizing: border-box; }
  html, body { width: 1200px; height: 1200px; overflow: hidden; }
  body {
    background: var(--stage);
    font-family: "Montserrat", sans-serif;
    position: relative;
  }
  .card {
    position: absolute;
    left: 150px;
    width: 900px;
    height: 514px;
    border-radius: 26px;
    overflow: hidden;
    box-shadow: 0 10px 24px rgba(0,0,0,0.18);
  }
  .card--front { top: 60px; background: var(--card-front); }
  .card--back {
    top: 626px;
    background: linear-gradient(135deg, var(--card-back-a), var(--card-back-b));
  }

  .brand {
    position: absolute;
    display: flex;
    align-items: center;
    gap: 22px;
  }
  .brand__dot {
    flex: none;
    border-radius: 50%;
    background: var(--red-soft);
  }
  .brand__name {
    color: var(--red);
    font-weight: 800;
    line-height: 1.05;
    text-transform: uppercase;
    letter-spacing: 0.5px;
  }
  .card--front .brand { left: 50%; top: 50%; transform: translate(-50%, -50%); }
  .card--front .brand__dot { width: 110px; height: 110px; }
  .card--front .brand__name { font-size: 44px; }

  .card--back .brand { left: 92px; top: 200px; gap: 16px; }
  .card--back .brand__dot { width: 74px; height: 74px; }
  .card--back .brand__name { font-size: 29px; }

  .divider {
    position: absolute;
    left: 458px;
    top: 92px;
    width: 3px;
    height: 278px;
    background: var(--blue);
  }
  .contact {
    position: absolute;
    left: 496px;
    top: 86px;
    color: var(--grey-text);
  }
  .contact__name { color: var(--red); font-weight: 800; font-size: 40px; line-height: 1.1; }
  .contact__title { font-size: 22px; font-weight: 500; margin-top: 4px; }
  .contact__address { font-size: 22px; font-weight: 500; line-height: 1.35; margin-top: 22px; }
  .contact__list { list-style: none; margin-top: 10px; }
  .contact__item {
    display: flex; align-items: center; gap: 14px;
    font-size: 22px; font-weight: 500; line-height: 1.55;
  }
  .contact__icon { width: 20px; height: 20px; flex: none; fill: var(--red); }
  .contact__domain { color: var(--blue); }

  .band {
    position: absolute; left: 0; bottom: 0;
    width: 100%; height: 30px; display: flex;
  }
  .band__blue { flex: 1; background: linear-gradient(90deg, var(--blue-mid), var(--blue)); }
  .band__red { flex: 1; background: var(--red); }
</style>
</head>
<body>
  <section class="card card--front" aria-label="Card front">
    <div class="brand">
      <span class="brand__dot"></span>
      <div class="brand__name">Crestline<br>Veterinary Blood Bank</div>
    </div>
  </section>

  <section class="card card--back" aria-label="Card back">
    <div class="brand">
      <span class="brand__dot"></span>
      <div class="brand__name">Crestline<br>Veterinary<br>Blood Bank</div>
    </div>

    <div class="divider"></div>

    <div class="contact">
      <div class="contact__name">Jordan Ellis</div>
      <div class="contact__title">Founder &amp; Director</div>
      <div class="contact__address">2750 Oak Ridge Rd<br>Fairview, VA 22030</div>
      <ul class="contact__list">
        <li class="contact__item">
          <svg class="contact__icon" viewBox="0 0 24 24" aria-hidden="true"><path d="M6.6 10.8a15.1 15.1 0 0 0 6.6 6.6l2.2-2.2a1 1 0 0 1 1-.25 11.4 11.4 0 0 0 3.6.57 1 1 0 0 1 1 1V20a1 1 0 0 1-1 1A17 17 0 0 1 3 4a1 1 0 0 1 1-1h3.5a1 1 0 0 1 1 1c0 1.25.2 2.45.57 3.57a1 1 0 0 1-.25 1z"/></svg>
          (555) 214-8830
        </li>
        <li class="contact__item">
          <svg class="contact__icon" viewBox="0 0 24 24" aria-hidden="true"><path d="M2 5h20v14H2z M2 5l10 8 10-8" fill="none" stroke="#e31e2a" stroke-width="0"/><path d="M2 6.5V19h20V6.5l-10 7.5z M3 5h18l-9 6.8z"/></svg>
          donate@crestlinevbb.com
        </li>
        <li class="contact__item">
          <svg class="contact__icon" viewBox="0 0 24 24" aria-hidden="true"><circle cx="12" cy="12" r="10"/><path d="M2 12h20M12 2c3 3 3 17 0 20M12 2c-3 3-3 17 0 20" fill="none" stroke="#fff" stroke-width="1.5"/></svg>
          <span>www.<span class="contact__domain">crestlinevbb</span>.com</span>
        </li>
      </ul>
    </div>

    <div class="band"><span class="band__blue"></span><span class="band__red"></span></div>
  </section>
</body>
</html>
```